Looking for a PowerPoint design for a Pharmaceutical Company

We need a PowerPoint template design to be used company-wide. We are a pharmaceutical company with 63 years of history and want to use a new template design to work more efficiently and effectively. Below are some of the things we are looking for in the new template design.

- Simple, modern, and professional

- Practical for every day use (easy to read, easy to create)

- Slides will be mainly projected or viewed on screens, but should also work fine when printed. (e.g. We do not want to use up our inks / toners printing several pages..)

- It would be great if you could provide us a list of colors that can be effectively used in the slides. (e.g. for highlighting fonts / multiple graph colors / etc.)

- Just as an FYI, our current logo image is (dark) blue. I am not uploading the logo image here because we do not want you to be limited by the current logo image. Depending on the design, we may / may not put our logo image on the slides.

Please feel free to reach out to me if you have any questions. I look forward to seeing your design. Thank you!

Target Market(s)

Pharmaceutical industry. (To be used internally and externally)

Industry/Entity Type

Pharmaceutical

Font styles to use
Sans Serif

Requirements
Must have
• Title slide, Subtitle slide, graphs, charts, tables, bullet points, and any other slide style components normally included.
Nice to have
• - As we are in the pharma industry, we want the slides to give credibility. But we do not want it look "old", "boring", or "typical". Feel free to use unique / fresh colors.
Should not have
• - TOO many colors
• - Please do not use the images on our website, which contain faces. (Any image with faces in it...) They are stock images we bought for the website, and we do not want the images on our slides. (e.g. image of running woman on the main page, image of a surgeon, image of kids playing soccer, etc.)
• - We are not looking for a design that is a modified version of our website design. We are looking for something new.

```html
<!DOCTYPE html>
<html lang="en">
<head>
<meta charset="utf-8">
<title>Pharmaceutical Presentation Template</title>
<link rel="stylesheet" href="https://fonts.googleapis.com/css2?family=Open+Sans:wght@400;600;700;800&display=swap">
<style>
:root{
  --blue:#1e6fad;
  --navy:#17395b;
  --sky:#4ea6dc;
  --pale:#e9f2f9;
  --ink:#2b3a4a;
  --muted:#8b97a4;
  --rule:#d6dde4;
  --white:#ffffff;
  --canvas:#d8dce1;
}
*{box-sizing:border-box;margin:0;padding:0}
html,body{width:889px;height:1200px;overflow:hidden}
body{background:var(--canvas);font-family:"Open Sans",Arial,sans-serif;color:var(--ink)}
.board{display:grid;grid-template-columns:repeat(3,283px);grid-template-rows:repeat(7,160px);gap:10px;padding:10px;width:889px;height:1200px}
.slide{position:relative;background:var(--white);overflow:hidden}
.abs{position:absolute}
.photo{position:absolute}
.photo-city{background:linear-gradient(180deg,#c9d3dc 0%,#a8b6c3 55%,#7d8d9c 100%)}
.photo-desk{background:linear-gradient(135deg,#3b4652 0%,#6e7a86 50%,#c4cbd2 100%)}
.photo-dusk{background:linear-gradient(180deg,#e2c9a6 0%,#b79a7c 45%,#5c5a60 100%)}
.photo-street{background:linear-gradient(180deg,#9fb2c4 0%,#6f7f8e 60%,#3d4650 100%)}
.photo-haze{background:linear-gradient(180deg,#d7dadc 0%,#b9aea0 60%,#8c8479 100%)}
.photo-bridge{background:linear-gradient(180deg,#b7c7d6 0%,#8ea2b4 60%,#5e6f7f 100%)}
.photo-green{background:linear-gradient(180deg,#a9b89a 0%,#6f7f5f 100%)}
.photo-road{background:linear-gradient(180deg,#b9c2a2 0%,#7b8463 55%,#4f5444 100%)}
.photo-tech{background:linear-gradient(135deg,#102a45 0%,#1e4c78 60%,#163a5e 100%)}
.photo-hands{background:linear-gradient(135deg,#1b1e23 0%,#3a3532 55%,#6a5a4d 100%)}
.title{font-weight:700;font-size:7px;color:var(--navy);text-transform:uppercase;letter-spacing:.2px;line-height:1.2}
.title-lg{font-weight:800;font-size:11px;color:var(--blue);text-transform:uppercase;letter-spacing:.3px}
.on-dark{color:var(--white)}
.kicker{font-size:4.2px;color:var(--muted);text-transform:uppercase;letter-spacing:.3px}
.label{font-weight:700;font-size:4.8px;color:var(--ink)}
.copy{font-size:3.9px;line-height:1.45;color:var(--muted)}
.copy.on-dark{color:#dbe7f2}
.contact-line{font-size:3.9px;line-height:1.45;color:var(--ink)}
.dot{position:absolute;width:12px;height:12px;border-radius:50%;background:var(--blue);display:flex;align-items:center;justify-content:center}
.dot svg{width:7px;height:7px}
.foot{position:absolute;right:0;bottom:0;width:70px;height:8px}
.rule{position:absolute;height:1px;background:var(--rule)}
.band{position:absolute;background:var(--blue)}
.tile{position:absolute;background:var(--blue);display:flex;flex-direction:column;align-items:center;justify-content:center;gap:3px}
.tile.dark{background:var(--navy)}
.tile svg{width:10px;height:10px}
.tile .label{color:var(--white);font-size:4.2px}
table.data{position:absolute;border-collapse:collapse;font-size:4px}
table.data th{background:var(--blue);color:var(--white);font-weight:700;padding:2.5px 4px;text-align:left}
table.data td{padding:2.5px 4px;color:var(--ink);border-bottom:1px solid var(--rule)}
table.data tr:nth-child(even) td{background:var(--pale)}
.section-word{font-weight:800;font-size:16px;color:var(--white);letter-spacing:.8px}
</style>
</head>
<body>
<svg width="0" height="0" style="position:absolute">
  <defs>
    <symbol id="ico-check" viewBox="0 0 10 10"><path d="M2 5.2l2 2 4-4.4" fill="none" stroke="#fff" stroke-width="1.3" stroke-linecap="round" stroke-linejoin="round"/></symbol>
    <symbol id="ico-chart" viewBox="0 0 10 10"><rect x="1.5" y="5" width="1.8" height="3.5" fill="#fff"/><rect x="4.1" y="3" width="1.8" height="5.5" fill="#fff"/><rect x="6.7" y="1.5" width="1.8" height="7" fill="#fff"/></symbol>
    <symbol id="ico-pin" viewBox="0 0 10 10"><path d="M5 9.2S2 5.8 2 4a3 3 0 0 1 6 0c0 1.8-3 5.2-3 5.2z" fill="#fff"/><circle cx="5" cy="4" r="1.1" fill="#1e6fad"/></symbol>
    <symbol id="ico-phone" viewBox="0 0 10 10"><path d="M2.3 1.5l1.6-.3 1 2.3-1 .8a5 5 0 0 0 1.8 1.8l.8-1 2.3 1-.3 1.6C6 8 1.9 4 2.3 1.5z" fill="#fff"/></symbol>
    <symbol id="ico-mail" viewBox="0 0 10 10"><rect x="1.2" y="2.5" width="7.6" height="5" rx=".6" fill="#fff"/><path d="M1.5 3l3.5 2.5L8.5 3" fill="none" stroke="#1e6fad" stroke-width=".7"/></symbol>
    <symbol id="ico-globe" viewBox="0 0 10 10"><circle cx="5" cy="5" r="3.6" fill="none" stroke="#fff" stroke-width=".9"/><ellipse cx="5" cy="5" rx="1.5" ry="3.6" fill="none" stroke="#fff" stroke-width=".7"/><path d="M1.4 5h7.2" stroke="#fff" stroke-width=".7"/></symbol>
    <symbol id="ico-gear" viewBox="0 0 10 10"><circle cx="5" cy="5" r="2.4" fill="none" stroke="#fff" stroke-width="1.6" stroke-dasharray="1.2 .8"/><circle cx="5" cy="5" r="1" fill="#fff"/></symbol>
    <symbol id="ico-arrow" viewBox="0 0 10 10"><path d="M2 5h5.5M5.2 2.6L7.6 5 5.2 7.4" fill="none" stroke="#fff" stroke-width="1.2" stroke-linecap="round" stroke-linejoin="round"/></symbol>
    <symbol id="foot-mark" viewBox="0 0 70 8"><polygon points="14,8 22,0 40,0 32,8" fill="#4ea6dc"/><polygon points="30,8 38,0 70,0 70,8" fill="#17395b"/></symbol>
  </defs>
</svg>

<main class="board">

  <!-- 1 Title slide -->
  <section class="slide slide-title">
    <div class="photo photo-city" role="img" aria-label="Hazy city skyline photograph" style="left:0;top:0;width:283px;height:96px"></div>
    <div class="band" style="left:0;top:96px;width:283px;height:2px"></div>
    <div class="abs title-lg" style="left:16px;top:110px">Presentation Title</div>
    <div class="abs kicker" style="left:16px;top:126px">Subtitle of presentation here</div>
    <svg class="foot"><use href="#foot-mark"/></svg>
  </section>

  <!-- 2 Alternate title -->
  <section class="slide slide-title-alt">
    <div class="photo photo-desk" role="img" aria-label="Photograph of hands typing on a laptop keyboard" style="left:92px;top:0;width:191px;height:72px"></div>
    <div class="band" style="left:0;top:72px;width:283px;height:38px"></div>
    <div class="abs" style="left:16px;top:80px;width:12px;height:12px;background:var(--navy)"></div>
    <div class="abs title-lg on-dark" style="left:34px;top:79px">Presentation Title</div>
    <div class="abs kicker" style="left:34px;top:95px;color:#cfe3f2">Subtitle of presentation here</div>
    <div class="abs copy" style="left:34px;top:118px;width:200px">Prepared for the annual review meeting. Department of research and development.</div>
    <svg class="foot"><use href="#foot-mark"/></svg>
  </section>

  <!-- 3 Six points -->
  <section class="slide slide-points">
    <div class="abs title" style="left:14px;top:10px">Presentation title goes here</div>
    <div class="abs kicker" style="left:14px;top:20px">Short subtitle text</div>
    <div class="dot" style="left:16px;top:38px"><svg><use href="#ico-check"/></svg></div>
    <div class="abs label" style="left:33px;top:38px">Research Quality</div>
    <div class="abs copy" style="left:33px;top:45px;width:100px">Clear short text describing this point in a line.</div>
    <div class="dot" style="left:16px;top:70px"><svg><use href="#ico-chart"/></svg></div>
    <div class="abs label" style="left:33px;top:70px">Market Growth</div>
    <div class="abs copy" style="left:33px;top:77px;width:100px">Clear short text describing this point in a line.</div>
    <div class="dot" style="left:16px;top:102px"><svg><use href="#ico-gear"/></svg></div>
    <div class="abs label" style="left:33px;top:102px">Production</div>
    <div class="abs copy" style="left:33px;top:109px;width:100px">Clear short text describing this point in a line.</div>
    <div class="dot" style="left:150px;top:38px"><svg><use href="#ico-globe"/></svg></div>
    <div class="abs label" style="left:167px;top:38px">Global Reach</div>
    <div class="abs copy" style="left:167px;top:45px;width:100px">Clear short text describing this point in a line.</div>
    <div class="dot" style="left:150px;top:70px"><svg><use href="#ico-arrow"/></svg></div>
    <div class="abs label" style="left:167px;top:70px">Next Steps</div>
    <div class="abs copy" style="left:167px;top:77px;width:100px">Clear short text describing this point in a line.</div>
    <div class="dot" style="left:150px;top:102px"><svg><use href="#ico-pin"/></svg></div>
    <div class="abs label" style="left:167px;top:102px">Locations</div>
    <div class="abs copy" style="left:167px;top:109px;width:100px">Clear short text describing this point in a line.</div>
    <svg class="foot"><use href="#foot-mark"/></svg>
  </section>

  <!-- 4 Photo with band -->
  <section class="slide slide-photo-band">
    <div class="photo photo-dusk" role="img" aria-label="City skyline at sunset photograph" style="left:0;top:0;width:283px;height:100px"></div>
    <div class="band" style="left:0;top:100px;width:283px;height:42px"></div>
    <div class="abs title on-dark" style="left:16px;top:108px">Presentation title goes here</div>
    <div class="abs copy on-dark" style="left:16px;top:119px;width:240px">Short supporting text explains the image above and gives context for the audience in two brief lines.</div>
    <svg class="foot"><use href="#foot-mark"/></svg>
  </section>

  <!-- 5 Photo left, list right -->
  <section class="slide slide-photo-list">
    <div class="photo photo-street" role="img" aria-label="City street between tall buildings photograph" style="left:0;top:0;width:112px;height:160px"></div>
    <div class="abs title" style="left:124px;top:12px">Presentation title goes here</div>
    <div class="dot" style="left:126px;top:32px"><svg><use href="#ico-check"/></svg></div>
    <div class="abs copy" style="left:143px;top:33px;width:125px">First point written as a short clear sentence here.</div>
    <div class="dot" style="left:126px;top:56px"><svg><use href="#ico-check"/></svg></div>
    <div class="abs copy" style="left:143px;top:57px;width:125px">Second point written as a short clear sentence here.</div>
    <div class="dot" style="left:126px;top:80px"><svg><use href="#ico-check"/></svg></div>
    <div class="abs copy" style="left:143px;top:81px;width:125px">Third point written as a short clear sentence here.</div>
    <div class="dot" style="left:126px;top:104px"><svg><use href="#ico-check"/></svg></div>
    <div class="abs copy" style="left:143px;top:105px;width:125px">Fourth point written as a short clear sentence here.</div>
    <svg class="foot"><use href="#foot-mark"/></svg>
  </section>

  <!-- 6 Text left, photo right -->
  <section class="slide slide-text-photo">
    <div class="photo photo-haze" role="img" aria-label="Aerial view of a city in haze photograph" style="left:150px;top:0;width:133px;height:160px"></div>
    <div class="band" style="left:110px;top:14px;width:120px;height:16px"></div>
    <div class="abs title on-dark" style="left:116px;top:19px;font-size:6px">Presentation title goes here</div>
    <div class="abs copy" style="left:14px;top:40px;width:128px">Body text sits on the left of the slide in short paragraphs. Keep each line readable on screen and in print.</div>
    <div class="abs copy" style="left:14px;top:66px;width:128px">A second paragraph adds detail to the topic and closes the idea with a clear message for readers.</div>
    <div class="abs copy" style="left:14px;top:92px;width:128px">Use one highlight colour for key figures and keep the rest of the text in grey.</div>
    <svg class="foot"><use href="#foot-mark"/></svg>
  </section>

  <!-- 7 Four tiles -->
  <section class="slide slide-tiles">
    <div class="abs title" style="left:14px;top:10px">Presentation title goes here</div>
    <div class="tile" style="left:14px;top:30px;width:60px;height:40px"><svg><use href="#ico-chart"/></svg><span class="label">Analysis</span></div>
    <div class="tile dark" style="left:78px;top:30px;width:60px;height:40px"><svg><use href="#ico-gear"/></svg><span class="label">Process</span></div>
    <div class="tile" style="left:142px;top:30px;width:60px;height:40px"><svg><use href="#ico-globe"/></svg><span class="label">Markets</span></div>
    <div class="tile dark" style="left:206px;top:30px;width:60px;height:40px"><svg><use href="#ico-check"/></svg><span class="label">Results</span></div>
    <div class="abs copy" style="left:14px;top:80px;width:252px">Each tile summarises one area of work. Add a short paragraph here to explain how the four areas connect and what the team will deliver in the coming quarter.</div>
    <div class="abs copy" style="left:14px;top:104px;width:252px">Keep copy brief so the slide stays clean and easy to read.</div>
    <svg class="foot"><use href="#foot-mark"/></svg>
  </section>

  <!-- 8 Banner with milestones -->
  <section class="slide slide-banner">
    <div class="abs title" style="left:14px;top:10px">Presentation title goes here</div>
    <div class="photo photo-bridge" role="img" aria-label="Bridge over a river photograph" style="left:0;top:26px;width:283px;height:56px"></div>
    <div class="dot" style="left:40px;top:76px"><svg><use href="#ico-check"/></svg></div>
    <div class="dot" style="left:104px;top:76px"><svg><use href="#ico-chart"/></svg></div>
    <div class="dot" style="left:168px;top:76px"><svg><use href="#ico-gear"/></svg></div>
    <div class="dot" style="left:232px;top:76px"><svg><use href="#ico-globe"/></svg></div>
    <div class="abs label" style="left:28px;top:94px;width:36px;text-align:center">Step One</div>
    <div class="abs label" style="left:92px;top:94px;width:36px;text-align:center">Step Two</div>
    <div class="abs label" style="left:156px;top:94px;width:36px;text-align:center">Step Three</div>
    <div class="abs label" style="left:220px;top:94px;width:36px;text-align:center">Step Four</div>
    <div class="abs copy" style="left:22px;top:102px;width:48px;text-align:center">Short note on this stage.</div>
    <div class="abs copy" style="left:86px;top:102px;width:48px;text-align:center">Short note on this stage.</div>
    <div class="abs copy" style="left:150px;top:102px;width:48px;text-align:center">Short note on this stage.</div>
    <div class="abs copy" style="left:214px;top:102px;width:48px;text-align:center">Short note on this stage.</div>
    <svg class="foot"><use href="#foot-mark"/></svg>
  </section>

  <!-- 9 Four photos -->
  <section class="slide slide-gallery">
    <div class="abs title" style="left:14px;top:10px">Presentation title goes here</div>
    <div class="photo photo-city" role="img" aria-label="Office building photograph" style="left:14px;top:28px;width:60px;height:44px"></div>
    <div class="photo photo-dusk" role="img" aria-label="Laboratory interior photograph" style="left:78px;top:28px;width:60px;height:44px"></div>
    <div class="photo photo-street" role="img" aria-label="Meeting room photograph" style="left:142px;top:28px;width:60px;height:44px"></div>
    <div class="photo photo-haze" role="img" aria-label="Warehouse photograph" style="left:206px;top:28px;width:60px;height:44px"></div>
    <div class="abs label" style="left:14px;top:78px">Headline</div>
    <div class="abs label" style="left:78px;top:78px">Headline</div>
    <div class="abs label" style="left:142px;top:78px">Headline</div>
    <div class="abs label" style="left:206px;top:78px">Headline</div>
    <div class="abs copy" style="left:14px;top:86px;width:58px">Brief caption text for this image area.</div>
    <div class="abs copy" style="left:78px;top:86px;width:58px">Brief caption text for this image area.</div>
    <div class="abs copy" style="left:142px;top:86px;width:58px">Brief caption text for this image area.</div>
    <div class="abs copy" style="left:206px;top:86px;width:58px">Brief caption text for this image area.</div>
    <svg class="foot"><use href="#foot-mark"/></svg>
  </section>

  <!-- 10 Three photos -->
  <section class="slide slide-trio">
    <div class="photo photo-green" role="img" aria-label="Green landscape photograph" style="left:14px;top:12px;width:82px;height:56px"></div>
    <div class="photo photo-road" role="img" aria-label="Country road photograph" style="left:100px;top:12px;width:82px;height:56px"></div>
    <div class="photo photo-bridge" role="img" aria-label="River and bridge photograph" style="left:186px;top:12px;width:82px;height:56px"></div>
    <div class="band" style="left:14px;top:60px;width:82px;height:8px"></div>
    <div class="band" style="left:100px;top:60px;width:82px;height:8px;background:var(--navy)"></div>
    <div class="band" style="left:186px;top:60px;width:82px;height:8px"></div>
    <div class="abs copy" style="left:14px;top:76px;width:80px">Short caption under the first image here.</div>
    <div class="abs copy" style="left:100px;top:76px;width:80px">Short caption under the second image here.</div>
    <div class="abs copy" style="left:186px;top:76px;width:80px">Short caption under the third image here.</div>
    <div class="abs title" style="left:14px;top:110px">Presentation title goes here</div>
    <div class="abs copy" style="left:14px;top:121px;width:250px">One closing line summarises the three images and links them to the topic.</div>
    <svg class="foot"><use href="#foot-mark"/></svg>
  </section>

  <!-- 11 Photo left, article right -->
  <section class="slide slide-article">
    <div class="photo photo-road" role="img" aria-label="Tree lined road photograph" style="left:0;top:0;width:128px;height:160px"></div>
    <div class="abs title" style="left:140px;top:14px">Presentation title goes here</div>
    <div class="abs label" style="left:140px;top:30px">Section heading</div>
    <div class="abs copy" style="left:140px;top:38px;width:128px">Body text explains the topic in short sentences. It reads well on screen and prints cleanly on paper with little ink.</div>
    <div class="abs copy" style="left:140px;top:66px;width:128px">Add a second paragraph for more detail. Keep lines short and use the accent blue only to mark key numbers.</div>
    <div class="abs copy" style="left:140px;top:94px;width:128px">Close with a single clear takeaway for the audience.</div>
    <svg class="foot"><use href="#foot-mark"/></svg>
  </section>

  <!-- 12 Hexagons -->
  <section class="slide slide-hex">
    <div class="abs title" style="left:14px;top:10px">Presentation title goes here</div>
    <svg class="abs" style="left:0;top:0" width="283" height="160" viewBox="0 0 283 160" aria-hidden="true">
      <g fill="#1e6fad">
        <polygon points="58,28 70,35 70,49 58,56 46,49 46,35"/>
        <polygon points="141,28 153,35 153,49 141,56 129,49 129,35" fill="#17395b"/>
        <polygon points="224,28 236,35 236,49 224,56 212,49 212,35"/>
        <polygon points="58,88 70,95 70,109 58,116 46,109 46,95" fill="#17395b"/>
        <polygon points="141,88 153,95 153,109 141,116 129,109 129,95"/>
        <polygon points="224,88 236,95 236,109 224,116 212,109 212,95" fill="#17395b"/>
      </g>
    </svg>
    <div class="abs copy" style="left:28px;top:61px;width:60px;text-align:center">Brief text for this item.</div>
    <div class="abs copy" style="left:111px;top:61px;width:60px;text-align:center">Brief text for this item.</div>
    <div class="abs copy" style="left:194px;top:61px;width:60px;text-align:center">Brief text for this item.</div>
    <div class="abs copy" style="left:28px;top:121px;width:60px;text-align:center">Brief text for this item.</div>
    <div class="abs copy" style="left:111px;top:121px;width:60px;text-align:center">Brief text for this item.</div>
    <div class="abs copy" style="left:194px;top:121px;width:60px;text-align:center">Brief text for this item.</div>
    <svg class="foot"><use href="#foot-mark"/></svg>
  </section>

  <!-- 13 Cycle -->
  <section class="slide slide-cycle">
    <div class="abs title" style="left:14px;top:10px">Presentation title goes here</div>
    <svg class="abs" style="left:106px;top:34px" width="72" height="72" viewBox="0 0 72 72" aria-hidden="true">
      <g fill="none" stroke-width="14">
        <path d="M36 8 A28 28 0 0 1 64 36" stroke="#1e6fad"/>
        <path d="M64 36 A28 28 0 0 1 36 64" stroke="#4ea6dc"/>
        <path d="M36 64 A28 28 0 0 1 8 36" stroke="#17395b"/>
        <path d="M8 36 A28 28 0 0 1 36 8" stroke="#8fc3e6"/>
      </g>
      <g stroke="#fff" stroke-width="2"><path d="M36 0v16M72 36H56M36 72V56M0 36h16"/></g>
    </svg>
    <div class="abs label" style="left:20px;top:40px">Plan</div>
    <div class="abs copy" style="left:20px;top:47px;width:76px">Short text for this phase.</div>
    <div class="abs label" style="left:20px;top:80px">Review</div>
    <div class="abs copy" style="left:20px;top:87px;width:76px">Short text for this phase.</div>
    <div class="abs label" style="left:190px;top:40px">Develop</div>
    <div class="abs copy" style="left:190px;top:47px;width:76px">Short text for this phase.</div>
    <div class="abs label" style="left:190px;top:80px">Deliver</div>
    <div class="abs copy" style="left:190px;top:87px;width:76px">Short text for this phase.</div>
    <svg class="foot"><use href="#foot-mark"/></svg>
  </section>

  <!-- 14 Percent rings -->
  <section class="slide slide-rings">
    <div class="abs title" style="left:14px;top:10px">Presentation title goes here</div>
    <svg class="abs" style="left:0;top:0" width="283" height="160" viewBox="0 0 283 160" aria-hidden="true">
      <g fill="none" stroke-width="5">
        <circle cx="58" cy="62" r="22" stroke="#e1e8ee"/>
        <circle cx="58" cy="62" r="22" stroke="#1e6fad" stroke-dasharray="117 138" transform="rotate(-90 58 62)"/>
        <circle cx="141" cy="62" r="22" stroke="#e1e8ee"/>
        <circle cx="141" cy="62" r="22" stroke="#17395b" stroke-dasharray="90 138" transform="rotate(-90 141 62)"/>
        <circle cx="224" cy="62" r="22" stroke="#e1e8ee"/>
        <circle cx="224" cy="62" r="22" stroke="#4ea6dc" stroke-dasharray="62 138" transform="rotate(-90 224 62)"/>
      </g>
      <g font-family="Open Sans, sans-serif" font-weight="700" font-size="8" fill="#17395b" text-anchor="middle">
        <text x="58" y="65">85%</text><text x="141" y="65">65%</text><text x="224" y="65">45%</text>
      </g>
    </svg>
    <div class="abs label" style="left:28px;top:94px;width:60px;text-align:center">Efficacy</div>
    <div class="abs label" style="left:111px;top:94px;width:60px;text-align:center">Adoption</div>
    <div class="abs label" style="left:194px;top:94px;width:60px;text-align:center">Coverage</div>
    <div class="abs copy" style="left:28px;top:102px;width:60px;text-align:center">Short note on this figure.</div>
    <div class="abs copy" style="left:111px;top:102px;width:60px;text-align:center">Short note on this figure.</div>
    <div class="abs copy" style="left:194px;top:102px;width:60px;text-align:center">Short note on this figure.</div>
    <svg class="foot"><use href="#foot-mark"/></svg>
  </section>

  <!-- 15 Donut chart -->
  <section class="slide slide-donut">
    <div class="abs title" style="left:14px;top:10px">Presentation title goes here</div>
    <svg class="abs" style="left:22px;top:30px" width="90" height="90" viewBox="0 0 90 90" aria-hidden="true">
      <g fill="none" stroke-width="18" transform="rotate(-90 45 45)">
        <circle cx="45" cy="45" r="32" stroke="#1e6fad" stroke-dasharray="80 201"/>
        <circle cx="45" cy="45" r="32" stroke="#17395b" stroke-dasharray="55 201" stroke-dashoffset="-80"/>
        <circle cx="45" cy="45" r="32" stroke="#4ea6dc" stroke-dasharray="40 201" stroke-dashoffset="-135"/>
        <circle cx="45" cy="45" r="32" stroke="#bcdcf0" stroke-dasharray="26 201" stroke-dashoffset="-175"/>
      </g>
    </svg>
    <div class="abs label" style="left:140px;top:36px;color:var(--blue)">Corporate market share</div>
    <div class="abs copy" style="left:140px;top:46px;width:128px">Explain what the chart shows in one or two short sentences so the figures are easy to read.</div>
    <div class="abs copy" style="left:140px;top:70px;width:128px">Segment one leads with forty percent of total volume this year.</div>
    <div class="abs copy" style="left:140px;top:86px;width:128px">Remaining segments share the balance across regions.</div>
    <svg class="foot"><use href="#foot-mark"/></svg>
  </section>

  <!-- 16 Bar chart -->
  <section class="slide slide-bars">
    <div class="abs title" style="left:14px;top:12px;width:90px">Presentation title goes here</div>
    <div class="abs copy" style="left:14px;top:36px;width:92px">Use this slide to compare values across years. Two colours keep the chart clear in print.</div>
    <div class="abs copy" style="left:14px;top:64px;width:92px">Add a short note on the main trend here.</div>
    <svg class="abs" style="left:116px;top:16px" width="156" height="122" viewBox="0 0 156 122" aria-hidden="true">
      <g stroke="#e1e8ee" stroke-width=".6"><path d="M8 20h146M8 45h146M8 70h146M8 95h146"/></g>
      <path d="M8 115h146" stroke="#b9c4ce" stroke-width=".8"/>
      <g fill="#1e6fad">
        <rect x="14" y="60" width="8" height="55"/><rect x="38" y="45" width="8" height="70"/><rect x="62" y="70" width="8" height="45"/><rect x="86" y="35" width="8" height="80"/><rect x="110" y="25" width="8" height="90"/><rect x="134" y="50" width="8" height="65"/>
      </g>
      <g fill="#8fc3e6">
        <rect x="23" y="78" width="8" height="37"/><rect x="47" y="65" width="8" height="50"/><rect x="71" y="85" width="8" height="30"/><rect x="95" y="58" width="8" height="57"/><rect x="119" y="48" width="8" height="67"/><rect x="143" y="72" width="8" height="43"/>
      </g>
    </svg>
    <svg class="foot"><use href="#foot-mark"/></svg>
  </section>

  <!-- 17 Table -->
  <section class="slide slide-table">
    <div class="abs title" style="left:14px;top:10px">Presentation title goes here</div>
    <table class="data" style="left:14px;top:28px;width:255px">
      <tr><th>Product</th><th>Region</th><th>Units</th><th>Growth</th></tr>
      <tr><td>Item A</td><td>North</td><td>12,400</td><td>8%</td></tr>
      <tr><td>Item B</td><td>South</td><td>9,800</td><td>5%</td></tr>
      <tr><td>Item C</td><td>East</td><td>7,250</td><td>11%</td></tr>
      <tr><td>Item D</td><td>West</td><td>6,100</td><td>3%</td></tr>
      <tr><td>Item E</td><td>Central</td><td>4,900</td><td>6%</td></tr>
      <tr><td>Total</td><td>All</td><td>40,450</td><td>7%</td></tr>
    </table>
    <svg class="foot"><use href="#foot-mark"/></svg>
  </section>

  <!-- 18 Quadrant circles -->
  <section class="slide slide-quad">
    <div class="abs title" style="left:14px;top:10px">Presentation title goes here</div>
    <svg class="abs" style="left:101px;top:28px" width="80" height="100" viewBox="0 0 80 100" aria-hidden="true">
      <circle cx="24" cy="30" r="20" fill="#1e6fad"/>
      <circle cx="56" cy="30" r="20" fill="#4ea6dc"/>
      <circle cx="24" cy="66" r="20" fill="#17395b"/>
      <circle cx="56" cy="66" r="20" fill="#8fc3e6"/>
      <circle cx="40" cy="48" r="13" fill="#fff"/>
      <circle cx="40" cy="48" r="9" fill="#1e6fad"/>
    </svg>
    <div class="abs label" style="left:16px;top:40px">Quality</div>
    <div class="abs copy" style="left:16px;top:47px;width:78px">Short text about this area.</div>
    <div class="abs label" style="left:16px;top:84px">Safety</div>
    <div class="abs copy" style="left:16px;top:91px;width:78px">Short text about this area.</div>
    <div class="abs label" style="left:190px;top:40px">Innovation</div>
    <div class="abs copy" style="left:190px;top:47px;width:78px">Short text about this area.</div>
    <div class="abs label" style="left:190px;top:84px">Access</div>
    <div class="abs copy" style="left:190px;top:91px;width:78px">Short text about this area.</div>
    <svg class="foot"><use href="#foot-mark"/></svg>
  </section>

  <!-- 19 Text with icon grid -->
  <section class="slide slide-features">
    <div class="abs title" style="left:14px;top:12px;width:100px">Presentation title goes here</div>
    <div class="abs copy" style="left:14px;top:36px;width:100px">A short introduction sets up the four features on the right. Keep it to a few lines.</div>
    <div class="abs copy" style="left:14px;top:62px;width:100px">Close with a simple call to action for the team.</div>
    <div class="dot" style="left:132px;top:30px"><svg><use href="#ico-check"/></svg></div>
    <div class="abs label" style="left:148px;top:30px">Feature</div>
    <div class="abs copy" style="left:148px;top:37px;width:56px">Short text line here.</div>
    <div class="dot" style="left:208px;top:30px"><svg><use href="#ico-chart"/></svg></div>
    <div class="abs label" style="left:224px;top:30px">Feature</div>
    <div class="abs copy" style="left:224px;top:37px;width:52px">Short text line here.</div>
    <div class="dot" style="left:132px;top:70px"><svg><use href="#ico-gear"/></svg></div>
    <div class="abs label" style="left:148px;top:70px">Feature</div>
    <div class="abs copy" style="left:148px;top:77px;width:56px">Short text line here.</div>
    <div class="dot" style="left:208px;top:70px"><svg><use href="#ico-globe"/></svg></div>
    <div class="abs label" style="left:224px;top:70px">Feature</div>
    <div class="abs copy" style="left:224px;top:77px;width:52px">Short text line here.</div>
    <svg class="foot"><use href="#foot-mark"/></svg>
  </section>

  <!-- 20 Section break -->
  <section class="slide slide-section">
    <div class="photo photo-tech" role="img" aria-label="Dark blue technology background photograph" style="left:0;top:0;width:283px;height:160px"></div>
    <div class="abs" style="left:70px;top:68px;width:22px;height:22px;border-radius:50%;border:1.5px solid var(--white)"></div>
    <div class="abs section-word" style="left:100px;top:67px">SECTION BREAKS</div>
    <div class="abs kicker" style="left:101px;top:88px;color:#b8d3ea">Short section subtitle</div>
    <svg class="foot"><use href="#foot-mark"/></svg>
  </section>

  <!-- 21 Contact -->
  <section class="slide slide-contact">
    <div class="band" style="left:0;top:0;width:140px;height:30px"></div>
    <div class="abs title on-dark" style="left:16px;top:11px;font-size:9px">Contact Us</div>
    <div class="dot" style="left:16px;top:44px"><svg><use href="#ico-phone"/></svg></div>
    <div class="abs contact-line" style="left:34px;top:47px">+1 555 0148</div>
    <div class="dot" style="left:16px;top:66px"><svg><use href="#ico-mail"/></svg></div>
    <div class="abs contact-line" style="left:34px;top:69px">hello@example.com</div>
    <div class="dot" style="left:16px;top:88px"><svg><use href="#ico-pin"/></svg></div>
    <div class="abs contact-line" style="left:34px;top:91px">120 Sample Street, Suite 4</div>
    <div class="dot" style="left:16px;top:110px"><svg><use href="#ico-globe"/></svg></div>
    <div class="abs contact-line" style="left:34px;top:113px">www.example.com</div>
    <div class="photo photo-hands" role="img" aria-label="Dark photograph of hands using a smartphone" style="left:140px;top:0;width:143px;height:160px"></div>
    <svg class="foot"><use href="#foot-mark"/></svg>
  </section>

</main>
</body>
</html>
```